Wine gifting platform needs redeem/decline page

Tavirel is a wine gifting platform. Users can send wine gifts to one or many people, the recipients will then receive an email with instructions on how to redeem their wine.

This is what we need: After clicking the link in the email they will be taken to the redeem/decline page/flow where they will choose their preferred wine and enter their shipping address. I have uploaded videos of both the decline and the redeem flows.

- All existing form fields, informational text, and error messages needs to be incorporated into the new design but otherwise you have creative freedom on presentation.
- We have four gift tiers: Silver, Gold, Platinum, and Diamond. We would like the redemption page to highlight this with different colors (or something else!) that's glanceable. I have attached screenshots to highlight these.
- Our target audience is professional and corporate but we want the redemption process to feel elegant and sleek. We want it to feel like a premium experience just like the wine they'll receive.

I would prefer Sketch files over Photoshop.

Target Market(s)

Professional, corporate

Number of Pages Required

3 page

Requirements
Must have
• All fields, all 3 steps of the wizard, information, and error messages/styles in the flow videos (attached)

```html
<!DOCTYPE html>
<html lang="en">
<head>
<meta charset="utf-8">
<title>Tavirel – Redeem Your Gift</title>
<link rel="stylesheet" href="https://fonts.googleapis.com/css2?family=Poppins:wght@400;500;600;700&family=Karla:wght@400;700&display=swap">
<style>
:root{
  --stage:#a8a8a8;
  --overlay:#8b8b8b;
  --white:#ffffff;
  --ink:#111111;
  --text:#2b2b2b;
  --blue:#0a3fae;
  --tint:#dfe6f7;
  --card:#f6f6f6;
  --field:#f3f3f3;
  --line:#eeeeee;
  --star:#f39a1d;
  --green:#2bb34a;
  --photo:#ececec;
}
*{box-sizing:border-box;margin:0;padding:0}
html,body{width:1200px;height:2792px;overflow:hidden;background:var(--stage)}
.canvas{position:absolute;left:0;top:0;width:1107px;height:2576px;transform:scale(1.0840);transform-origin:0 0;font-family:'Poppins',sans-serif;color:var(--ink)}
.abs{position:absolute}
.panel{position:absolute;left:60px;width:987px;background:var(--white)}
.brand{position:absolute;left:0;width:987px;text-align:center;font-family:'Poppins',sans-serif;font-weight:600;font-size:44px;color:var(--blue);letter-spacing:1px}
.step-line{position:absolute;height:3px;background:var(--line)}
.step-dot{position:absolute;width:38px;height:38px;border-radius:50%;background:var(--line);color:var(--blue);font-weight:700;font-size:15px;display:flex;align-items:center;justify-content:center}
.step-dot.active{background:var(--blue);color:var(--white)}
.step-label{position:absolute;width:220px;text-align:center;font-weight:700;font-size:14px}
.intro{left:119px;top:215px;width:750px;height:129px;background:var(--tint);border-radius:8px;padding:26px 25px}
.intro h2{font-size:17px;font-weight:700;margin-bottom:8px}
.intro p{font-family:'Karla',sans-serif;font-size:10.6px;line-height:19.5px;color:var(--text)}
.section-title{left:0;width:987px;text-align:center;font-size:18px;font-weight:700}
.scrollbar{width:8px;background:var(--line);border-radius:4px}
.scrollbar i{position:absolute;left:1px;width:6px;background:var(--blue);border-radius:3px}
.wine-card{position:absolute;top:446px;width:155px;height:221px;background:var(--card);border-radius:8px;text-align:center}
.wine-card.active{background:var(--white);height:270px;box-shadow:0 4px 14px rgba(0,0,0,.14)}
.wine-card .bottle{position:absolute;left:62px;top:38px;width:30px;height:102px;border-radius:6px 6px 4px 4px;background:linear-gradient(#3a1a1e,#1c0d10)}
.wine-card .stars{position:absolute;left:0;width:100%;top:162px;color:var(--star);font-size:7px;letter-spacing:1px}
.wine-card .name{position:absolute;left:0;width:100%;top:176px;font-size:15px;font-weight:600;color:#333;line-height:21px}
.wine-card .accent{position:absolute;left:46px;top:-3px;width:62px;height:3px;background:var(--blue)}
.btn{position:absolute;display:flex;align-items:center;justify-content:center;font-weight:700;font-size:9px;border-radius:2px}
.btn.primary{background:var(--blue);color:var(--white)}
.btn.plain{background:var(--line);color:var(--ink)}
.overlay{position:absolute;left:60px;top:890px;width:987px;height:750px;background:var(--overlay)}
.modal{position:absolute;left:96px;top:910px;width:917px;height:700px;background:var(--white);border-radius:4px;font-family:'Karla',sans-serif;color:var(--text)}
.close-x{position:absolute;width:26px;height:26px;border-radius:50%;background:var(--blue);border:2px solid var(--white);color:var(--white);font:700 13px 'Poppins',sans-serif;display:flex;align-items:center;justify-content:center}
.modal .photo{position:absolute;left:24px;top:29px;width:235px;height:328px;background:var(--photo)}
.modal .photo span{position:absolute;left:86px;top:52px;width:56px;height:216px;border-radius:10px 10px 6px 6px;background:linear-gradient(90deg,#140a0c,#3a2226,#140a0c)}
.modal h1{position:absolute;left:289px;top:40px;font-family:'Poppins',sans-serif;font-size:23px;font-weight:600;color:var(--ink)}
.modal .desc{position:absolute;left:284px;top:88px;width:610px;font-size:12.6px;line-height:25.5px}
.modal .details{position:absolute;left:30px;top:383px;width:860px;font-size:12.6px;line-height:25.5px}
.modal b{color:var(--ink)}
.field-label{position:absolute;font-weight:700;font-size:11.5px}
.field{position:absolute;height:46px;background:var(--field);border-radius:6px;font-family:'Karla',sans-serif;font-size:12.5px;color:var(--text);display:flex;align-items:center;padding-left:28px}
.check{position:absolute;left:118px;width:16px;height:16px;border:1.5px solid #444;border-radius:3px}
.check-text{position:absolute;left:140px;font-family:'Karla',sans-serif;font-size:12.5px;color:var(--text)}
.check-text a{color:var(--blue);text-decoration:none}
</style>
</head>
<body>
<div class="canvas">

  <!-- Step 1: choose gift -->
  <section class="panel" style="top:69px;height:750px">
    <div class="brand" style="top:15px">Tavirel</div>
    <div class="step-line" style="left:242px;top:133px;width:533px"></div>
    <div class="step-dot" style="left:223px;top:115px">01</div>
    <div class="step-dot" style="left:484px;top:115px">02</div>
    <div class="step-dot" style="left:755px;top:115px">03</div>
    <div class="step-label" style="left:135px;top:165px">CHOOSE YOUR GIFT</div>
    <div class="step-label" style="left:396px;top:165px">ENTER YOUR ADDRESS</div>
    <div class="step-label" style="left:668px;top:165px">CONFIRM</div>

    <div class="abs intro">
      <h2>DIAMOND COLLECTION</h2>
      <p>Lorem ipsum dolor sit amet, consectetur adipiscing elit, sed do eiusmod tempor incididunt ut labore et dolore magna aliqua. Quis ipsum suspendisse ultrices gravida. Risus commodo viverra maecenas accumsan lacus vel facilisis.</p>
    </div>

    <div class="abs section-title" style="top:383px">CHOOSE YOUR GIFT FORM THE DIAMOND COLLECTION</div>
    <div class="abs scrollbar" style="left:962px;top:349px;height:375px"><i style="top:37px;height:105px"></i></div>

    <div class="wine-card" style="left:62px"><div class="bottle" role="img" aria-label="Pinot Noir bottle photo"></div><div class="stars">★★★★★</div><div class="name">Pinot Noir</div></div>
    <div class="wine-card" style="left:234px"><div class="bottle" role="img" aria-label="Sangiovese bottle photo"></div><div class="stars">★★★★★</div><div class="name">Sangiovese</div></div>
    <div class="wine-card active" style="left:415px"><div class="accent"></div><div class="bottle" role="img" aria-label="Cabernet Sauvignon bottle photo"></div><div class="stars">★★★★★</div><div class="name">Cabernet<br>Sauvignon</div><div class="btn primary" style="left:32px;top:229px;width:90px;height:22px;font-size:7px">SHOP NOW</div></div>
    <div class="wine-card" style="left:591px"><div class="bottle" role="img" aria-label="Grenache bottle photo"></div><div class="stars">★★★★★</div><div class="name">Grenache</div></div>
    <div class="wine-card" style="left:763px"><div class="bottle" role="img" aria-label="Syrah bottle photo"></div><div class="stars">★★★★★</div><div class="name">Syrah</div></div>
  </section>

  <!-- Gift details modal -->
  <div class="overlay"></div>
  <div class="abs" style="left:1022px;top:1240px;width:8px;height:375px;background:#7d7d7d;border-radius:4px"><i style="position:absolute;left:1px;top:37px;width:6px;height:105px;background:#0b2f7e;border-radius:3px"></i></div>
  <div class="modal">
    <div class="photo" role="img" aria-label="Red blend wine bottle photo"><span></span></div>
    <h1>Red Blend from our Silver Collection</h1>
    <p class="desc">A red wine blend is any red wine that is not made with one specific variety. A red wine blend can theoretically be made of any combination of red grape varieties. The red wine blend might be made potentially of Cabernet Sauvignon, Merlot, Cabernet Franc, Malbec, Petite Verdot, and Carrnenere, as prescribed in Bordeaux. Tradi-tionally, wines have been blended to ensure that there are sufficient levels of alcohol, acidity, tannin, and fruit extract that will increase the likelihood for aging ability, ensuring that the wine will have interesting flavors years from now. By blending wines made frorn different varieties, the winemaker can combine the best as-pects of two or three grape varieties into one final product.<br><b>Wine Body:</b> Dependng on the potential blend of grapes, red blends can vary in body and acidity.<br><b>Wine Pairings:</b> Red blends vary in flavor, body, acidity, and alcohol content, but as a general guideline, they are most likely to pair with richer entrees and meat dishes. Best Served At 60-68F Growing Region,. France, USA, Italy, Chile</p>
    <p class="details"><b>Producers:</b> Opal Crest, Napa Valley, USA. Chateau Verlaine-Dumont, Pauillac, France. Chateau Marbrel, Saint-Estephe, France. Chateau Lisandre, Saint-Julien, France. Chateau Orvand, Saint-Julien, France. Chateau Belcourt-Rive, Saint-Estephe, France. Chateau Vessane, Pessac-Leognan, France. Chateau Hautclair, Pessac-Leognan, France. Chateau Morvelle, Saint-Julien, France. Chateau Dunereau, Saint-Julien, France. Valmira, Aconcagua Valley, Chile<br><b>Units: 1</b><br>Past Selections Include...<br>Ashby &amp; Ashby Red Blend 2019<br>Blackberry, white pepper, black licorice, cocoa with hints of smoked meat. Long and energetic finish that builds with floral notes. Blend: 5896 Syrah, 42% Cabernet Sauvignon<br>Previous recipients of this gift package have received this product. Actual gift will vary based on availability but will be comparable.</p>
    <div class="btn plain" style="left:641px;top:653px;width:81px;height:27px">CLOSE</div>
    <div class="btn primary" style="left:732px;top:653px;width:144px;height:27px">SELECT THIS GIFT PACKAGE</div>
  </div>
  <div class="close-x" style="left:995px;top:905px">✕</div>

  <!-- Step 2: address -->
  <section class="panel" style="top:1711px;height:796px">
    <div class="brand" style="top:17px">Tavirel</div>
    <div class="close-x" style="left:935px;top:34px">✕</div>
    <div class="step-line" style="left:242px;top:133px;width:533px"></div>
    <div class="step-dot" style="left:223px;top:115px"><svg width="14" height="14" viewBox="0 0 14 14"><path d="M2 7.5l3.2 3L12 3.5" fill="none" stroke="var(--green)" stroke-width="2.2" stroke-linecap="round" stroke-linejoin="round"/></svg></div>
    <div class="step-dot active" style="left:484px;top:115px">02</div>
    <div class="step-dot" style="left:755px;top:115px">03</div>
    <div class="step-label" style="left:135px;top:164px">CHOOSE YOUR GIFT</div>
    <div class="step-label" style="left:396px;top:164px">ENTER YOUR ADDRESS</div>
    <div class="step-label" style="left:668px;top:164px">CONFIRM</div>

    <div class="field-label" style="left:111px;top:241px">FIRST NAME</div>
    <div class="field-label" style="left:519px;top:241px">LAST NAME</div>
    <div class="field" style="left:103px;top:274px;width:378px;padding-left:20px">AA</div>
    <div class="field" style="left:509px;top:274px;width:378px;padding-left:22px">FF</div>

    <div class="field-label" style="left:113px;top:344px">EMAIL ADDRESS</div>
    <div class="field-label" style="left:521px;top:344px">PHONE#</div>
    <div class="field" style="left:103px;top:377px;width:378px;padding-left:20px">AA</div>
    <div class="field" style="left:509px;top:377px;width:378px;padding-left:22px">FF</div>

    <div class="field-label" style="left:113px;top:446px">ADDRESS</div>
    <div class="field-label" style="left:521px;top:446px">ADDRESS (APT/FLOOR/SUITE)</div>
    <div class="field" style="left:103px;top:479px;width:378px">Address</div>
    <div class="field" style="left:509px;top:479px;width:378px">Address (Apt/Floor/Suite)</div>

    <div class="field-label" style="left:113px;top:545px">CITY</div>
    <div class="field-label" style="left:383px;top:545px">STATE</div>
    <div class="field-label" style="left:651px;top:545px">POSTAL CODE</div>
    <div class="field" style="left:103px;top:577px;width:249px">City</div>
    <div class="field" style="left:373px;top:577px;width:249px">State</div>
    <div class="field" style="left:642px;top:577px;width:249px">Postal Code</div>

    <div class="check" style="top:652px;border-color:var(--green)"><svg width="13" height="13" viewBox="0 0 14 14" style="position:absolute;left:0;top:0"><path d="M3 7.5l2.7 2.6L11 4.2" fill="none" stroke="var(--green)" stroke-width="1.8" stroke-linecap="round" stroke-linejoin="round"/></svg></div>
    <div class="check-text" style="top:652px">I want to subscribe To Emails From Tavirel to learn how to quickly and esily Send Wine Gifts.</div>
    <div class="check" style="top:693px"></div>
    <div class="check-text" style="top:693px">I Confirm That I am Of Legal Drinking Age in may State.</div>
    <div class="check" style="top:730px"></div>
    <div class="check-text" style="top:730px">I agree to the <a>Privacy Policy</a> and <a>terms of service.</a></div>

    <div class="btn plain" style="left:686px;top:724px;width:83px;height:28px">BACK</div>
    <div class="btn primary" style="left:783px;top:724px;width:91px;height:28px">NEXT</div>
  </section>

</div>
</body>
</html>
```